Bright Fern Custom Homes business card. Double sided. Modern. professional

Bright Fern Custom Homes
contemporary modern design with our logo /
Double sided with all our contact information
Use same Green colors as in our Logo. Contemporary logo that grabs your attention. Visually pleasing and balanced. Easy to read, and Vibrant. Would love an option for rounded edges. Embossed logo would be amazing.
Contact Information for Business Card
Dana Welk Owner / General Contractor Bright Fern Custom Homes p: 704.552.1830 m: 912.648.2071 e: brightferncustomhomes@mailbox.example w: www.brightferncustomhomes.example 218 Pryor Meadow Lane Fernridge, NC 28041

```html
<!DOCTYPE html>
<html lang="en">
<head>
<meta charset="utf-8">
<title>Bright Fern Custom Homes – Business Card</title>
<link rel="stylesheet" href="https://fonts.googleapis.com/css2?family=Allura&family=Roboto:wght@400;500;700&display=swap">
<style>
  :root {
    --backdrop: #a9a9a9;
    --card-cream: #d2c1ab;
    --card-green: #5c6f31;
    --brand-green: #5f7a33;
    --deep-green: #4f6129;
    --ink: #141414;
    --muted: #7b7062;
    --label: #8a7d6c;
  }
  * { margin: 0; padding: 0; box-sizing: border-box; }
  html, body { width: 1200px; height: 1000px; overflow: hidden; }
  body {
    background: var(--backdrop);
    font-family: "Roboto", Arial, sans-serif;
    position: relative;
  }
  .card {
    position: absolute;
    width: 353px;
    height: 613px;
    border-radius: 22px;
  }
  .card--front { left: 198px; top: 191px; background: var(--card-cream); }
  .card--back  { left: 651px; top: 196px; background: var(--card-green); }

  .brand {
    position: absolute;
    left: 28px; top: 42px;
    display: flex; align-items: center; gap: 14px;
    color: var(--brand-green);
    font-weight: 400;
  }
  .brand__dot {
    width: 64px; height: 64px; border-radius: 50%;
    background: var(--brand-green);
  }
  .brand__name { font-size: 21px; letter-spacing: 2px; line-height: 1; display: block; margin-top: 10px; }
  .brand__sub { font-size: 8px; letter-spacing: 4.6px; display: block; margin-top: 3px; padding-left: 36px; }

  .holder__name {
    position: absolute; left: 38px; top: 238px;
    font-family: "Allura", cursive;
    font-weight: 400;
    font-size: 60px; color: var(--ink); line-height: 1;
  }
  .holder__title {
    position: absolute; left: 39px; top: 311px;
    font-size: 13px; font-weight: 700; letter-spacing: 1.5px;
    color: var(--label);
  }
  .rule {
    position: absolute; height: 3px; background: var(--brand-green);
  }
  .rule--one { left: 39px; top: 344px; width: 64px; }
  .rule--two { left: 38px; top: 440px; width: 71px; }

  .address {
    position: absolute; left: 41px; top: 383px;
    font-size: 14px; line-height: 18px; color: var(--muted);
    font-style: normal;
  }
  .contacts {
    position: absolute; left: 41px; top: 465px;
    list-style: none; font-size: 14px; line-height: 17.5px; color: var(--muted);
  }
  .contacts li { display: flex; align-items: center; gap: 7px; white-space: nowrap; }
  .contacts svg { width: 12px; height: 12px; fill: var(--brand-green); flex: none; }

  .back-mark {
    position: absolute; left: 0; right: 0; top: 205px;
    text-align: center; color: var(--deep-green); font-weight: 400;
  }
  .back-mark__dot {
    width: 120px; height: 120px; border-radius: 50%;
    background: var(--deep-green); margin: 0 auto 36px;
  }
  .back-mark__name { font-size: 36px; letter-spacing: 3px; line-height: 1; }
  .back-mark__sub { font-size: 10px; letter-spacing: 7px; margin-top: 8px; }
</style>
</head>
<body>
  <section class="card card--front" aria-label="Card front">
    <div class="brand">
      <span class="brand__dot"></span>
      <span><span class="brand__name">BRIGHT FERN</span><span class="brand__sub">CUSTOM HOMES</span></span>
    </div>

    <h1 class="holder__name">Dana Welk</h1>
    <p class="holder__title">OWNER</p>
    <div class="rule rule--one"></div>

    <address class="address">218 Pryor Meadow Lane,<br>Fernridge, NC 28041</address>
    <div class="rule rule--two"></div>

    <ul class="contacts">
      <li><svg viewBox="0 0 24 24"><path d="M6.6 10.8a15.1 15.1 0 0 0 6.6 6.6l2.2-2.2c.3-.3.7-.4 1-.2 1.1.4 2.3.6 3.6.6.6 0 1 .4 1 1V20c0 .6-.4 1-1 1A17 17 0 0 1 3 4c0-.6.4-1 1-1h3.5c.6 0 1 .4 1 1 0 1.3.2 2.5.6 3.6.1.3 0 .7-.2 1z"/></svg>704.552.1830</li>
      <li><svg viewBox="0 0 24 24"><path d="M7 1h10a2 2 0 0 1 2 2v18a2 2 0 0 1-2 2H7a2 2 0 0 1-2-2V3a2 2 0 0 1 2-2zm0 3v14h10V4zm5 15.2a1.2 1.2 0 1 0 0 2.4 1.2 1.2 0 0 0 0-2.4z"/></svg>912.648.2071</li>
      <li><svg viewBox="0 0 24 24"><path d="M2 5h20v14H2zm2.4 2L12 11.8 19.6 7zM4 8.8V17h16V8.8l-8 5z"/></svg>brightferncustomhomes@mailbox.example</li>
      <li><svg viewBox="0 0 24 24"><path d="M12 2a10 10 0 1 0 0 20 10 10 0 0 0 0-20zm6.9 6h-3a15 15 0 0 0-1.3-3.9A8 8 0 0 1 18.9 8zM12 4c.8 1.2 1.5 2.5 1.9 4h-3.8c.4-1.5 1.1-2.8 1.9-4zM4.3 14a8 8 0 0 1 0-4h3.4a16 16 0 0 0 0 4zm.8 2h3a15 15 0 0 0 1.3 3.9A8 8 0 0 1 5.1 16zm3-8h-3a8 8 0 0 1 4.3-3.9C8.8 5.3 8.4 6.6 8.1 8zM12 20c-.8-1.2-1.5-2.5-1.9-4h3.8c-.4 1.5-1.1 2.8-1.9 4zm2.3-6H9.7a14 14 0 0 1 0-4h4.6a14 14 0 0 1 0 4zm.3 5.9c.6-1.2 1-2.5 1.3-3.9h3a8 8 0 0 1-4.3 3.9zm1.7-5.9a16 16 0 0 0 0-4h3.4a8 8 0 0 1 0 4z"/></svg>brightferncustomhomes.example</li>
    </ul>
  </section>

  <section class="card card--back" aria-label="Card back">
    <div class="back-mark">
      <div class="back-mark__dot"></div>
      <p class="back-mark__name">BRIGHT FERN</p>
      <p class="back-mark__sub">CUSTOM HOMES</p>
    </div>
  </section>
</body>
</html>
```